KVO-Business Card Design

I need a modern, professional business card design that includes my logo as the main feature, maybe the entire background with the contact info overlaying or even contact info on the back and the logo full frontal

Neat and organized placement of contact information

Would like to see options in black and white

Target Market(s)

real estate Developers, Construction managers, business and home owners

Industry/Entity Type

Construction

Contact Information for Business Card

KVO Construction
Danny Ferrante
General Contractor

Office: 1-888-902-7315 Ext #1
Cell: 215-730-4162
Fax: 1-888-902-7315

Font styles to use
Serif

Requirements
Must have
• title
• office #
• cell #
• Email
• website
Nice to have
• fax

```html
<!DOCTYPE html>
<html lang="en">
<head>
<meta charset="utf-8">
<title>KVO Construction – Business Card</title>
<link rel="stylesheet" href="https://fonts.googleapis.com/css2?family=Questrial&family=Mulish:wght@700;800&display=swap">
<style>
  :root {
    --stage: #eef0ef;
    --card-black: #0b0b0b;
    --card-white: #ffffff;
    --green-deep: #1f7a35;
    --green-mid: #3ea447;
    --green-lime: #7cc242;
    --ink: #1a1a1a;
    --paper-text: #ffffff;
  }
  * { box-sizing: border-box; margin: 0; padding: 0; }
  html, body {
    width: 1200px; height: 800px; overflow: hidden;
    background: var(--stage);
  }
  .canvas { position: relative; width: 1200px; height: 800px; }

  .card {
    position: absolute;
    overflow: hidden;
    box-shadow: 0 6px 18px rgba(0,0,0,0.12);
  }

  /* Front: logo side */
  .card-front {
    left: 90px; top: 102px; width: 340px; height: 596px;
    background: var(--card-black);
    display: flex; align-items: center; justify-content: center;
  }
  .brand-name {
    font-family: "Mulish", sans-serif;
    font-weight: 800;
    color: var(--green-mid);
    white-space: nowrap;
  }
  .card-front .brand-name { font-size: 30px; letter-spacing: 0.5px; }
  .brand-mark {
    display: inline-block; width: 14px; height: 14px;
    background: var(--green-mid); margin-right: 10px; vertical-align: middle;
  }
  .card-front .brand-mark { width: 18px; height: 18px; }

  /* Back: contact side */
  .card-back {
    left: 490px; top: 223px; width: 620px; height: 354px;
    background: var(--card-white);
  }
  .card-back .wave { position: absolute; inset: 0; width: 620px; height: 354px; }
  .card-back .brand {
    position: absolute; left: 40px; top: 88px;
  }
  .card-back .brand-name { font-size: 28px; }

  .holder {
    position: absolute; right: 38px; top: 30px;
    text-align: right;
    padding-right: 12px;
    border-right: 2px solid var(--green-deep);
  }
  .holder-name {
    font-family: "Questrial", sans-serif;
    font-size: 21px; color: var(--ink); line-height: 1.1;
  }
  .holder-title {
    font-family: "Mulish", sans-serif;
    font-weight: 700; font-size: 13px; color: var(--green-deep);
    margin-top: 2px;
  }

  .contact-list {
    position: absolute; right: 26px; top: 165px;
    list-style: none;
    font-family: "Questrial", sans-serif;
    font-size: 14px; color: var(--paper-text);
    text-align: right;
  }
  .contact-list li {
    display: flex; align-items: center; justify-content: flex-end;
    height: 19px; gap: 8px;
  }
  .contact-icon { width: 14px; height: 14px; flex: none; }

  .website {
    position: absolute; left: 0; width: 560px; top: 308px;
    text-align: center;
    font-family: "Questrial", sans-serif;
    font-size: 16px; color: var(--paper-text); letter-spacing: 0.3px;
  }
</style>
</head>
<body>
<main class="canvas">

  <section class="card card-front" aria-label="Card front">
    <div class="brand"><span class="brand-mark"></span><span class="brand-name">KVO Construction</span></div>
  </section>

  <section class="card card-back" aria-label="Card back">
    <svg class="wave" viewBox="0 0 620 354" aria-hidden="true">
      <path d="M0,272 C150,282 300,204 420,152 C490,122 560,117 620,120 L620,354 L0,354 Z" fill="var(--card-black)"/>
      <path d="M0,254 C150,266 300,190 420,138 C490,110 560,102 620,104 L620,120 C560,117 490,122 420,152 C300,204 150,282 0,272 Z" fill="var(--green-deep)"/>
      <path d="M0,262 C150,276 300,198 420,146" fill="none" stroke="var(--green-lime)" stroke-width="4"/>
      <path d="M210,262 C300,236 370,206 440,170" fill="none" stroke="var(--green-lime)" stroke-width="3" stroke-linecap="round"/>
    </svg>

    <div class="brand"><span class="brand-mark"></span><span class="brand-name">KVO Construction</span></div>

    <div class="holder">
      <p class="holder-name">Danny Ferrante</p>
      <p class="holder-title">General Contractor</p>
    </div>

    <ul class="contact-list">
      <li><span>215-730-4162</span>
        <svg class="contact-icon" viewBox="0 0 14 14" aria-label="Cell"><circle cx="7" cy="7" r="7" fill="var(--green-lime)"/><rect x="4.5" y="3" width="5" height="8" rx="1" fill="none" stroke="#111" stroke-width="1.2"/></svg></li>
      <li><span>1-888-902-7315 Ext #1</span>
        <svg class="contact-icon" viewBox="0 0 14 14" aria-label="Office"><circle cx="7" cy="7" r="7" fill="var(--green-lime)"/><path d="M4,3.5 L5.6,3.5 L6.2,5.5 L5.2,6.3 C5.7,7.4 6.6,8.3 7.7,8.8 L8.5,7.8 L10.5,8.4 L10.5,10 C7,10.2 3.8,7 4,3.5 Z" fill="#111"/></svg></li>
      <li><span>1-888-902-7315</span>
        <svg class="contact-icon" viewBox="0 0 14 14" aria-label="Fax"><circle cx="7" cy="7" r="7" fill="var(--green-lime)"/><rect x="4" y="6" width="6" height="4" fill="#111"/><rect x="5" y="3.5" width="4" height="2.5" fill="none" stroke="#111" stroke-width="1"/></svg></li>
      <li><span>office@kvoconstruction.com</span>
        <svg class="contact-icon" viewBox="0 0 14 14" aria-label="Email"><rect x="1" y="3" width="12" height="8" fill="var(--green-lime)"/><path d="M1,3 L7,8 L13,3" fill="none" stroke="#111" stroke-width="1"/></svg></li>
    </ul>

    <p class="website">www.website.com</p>
  </section>

</main>
</body>
</html>
```